Mark & Lisa's Hammock Season Party

Invitation to a party 60-80 people at a private residence. Age range 30-40s.

Themes: summer/casual/Australian backyard/local community

**For delivery via both email and printed copy**
Would like one document suitable for both purposes or two versions for electronic or paper invitation. I will arrange printing so please prepare it in a suitable format.

Specimen text attached. Address and phone contact to follow by message with successful bidder

Thanks!
Mark

Target Market(s)

Locals, friends. Party attendees will typicaly be parents in their forties who who be leaving the kids at home for a relaxed party night, and walking home afterward

Industry/Entity Type

Community

Font styles to use
Sans Serif

Requirements
Should not have
• Cliche Australiana imagery. No kangaroos etc

```html
<!DOCTYPE html>
<html lang="en">
<head>
<meta charset="utf-8">
<title>Mark &amp; Lisa's Hammock Season Party – Details</title>
<link rel="stylesheet" href="https://fonts.googleapis.com/css2?family=Poiret+One&display=swap">
<style>
  :root {
    --ink: #ebe7df;
    --ground-dark: #1c1c1c;
    --ground-mid: #2e2d2b;
    --ground-light: #3a3936;
  }
  html, body {
    margin: 0;
    padding: 0;
    width: 800px;
    height: 1200px;
    overflow: hidden;
    background: var(--ground-dark);
  }
  .invite {
    position: relative;
    width: 800px;
    height: 1200px;
    overflow: hidden;
    font-family: "Poiret One", sans-serif;
    color: var(--ink);
  }
  .backdrop {
    position: absolute;
    inset: 0;
    background:
      radial-gradient(ellipse at 30% 25%, var(--ground-light) 0%, transparent 55%),
      radial-gradient(ellipse at 75% 65%, var(--ground-mid) 0%, transparent 60%),
      linear-gradient(180deg, var(--ground-mid) 0%, var(--ground-dark) 100%);
  }
  .line {
    position: absolute;
    left: 0;
    width: 800px;
    text-align: center;
    white-space: nowrap;
    letter-spacing: 0.08em;
    font-size: 27px;
    line-height: 1;
    transform: translateY(-50%);
  }
  .line .aside { font-style: italic; }
  .line .big { font-size: 34px; letter-spacing: 0.02em; }
  .details-1 { top: 187px; }
  .details-2 { top: 260px; }
  .details-3 { top: 330px; }
  .details-4 { top: 403px; }
  .friends-1 { top: 620px; font-size: 25px; }
  .friends-2 { top: 693px; font-size: 25px; }
  .friends-3 { top: 765px; font-size: 25px; }
  .rsvp-1 { top: 908px; font-size: 27px; }
  .rsvp-2 { top: 981px; font-size: 25px; }
</style>
</head>
<body>
<main class="invite">
  <div class="backdrop" role="img" aria-label="Dark weathered concrete wall texture"></div>

  <p class="line details-1"><span class="big">C</span>hild-free event</p>
  <p class="line details-2"><span class="big">D</span>ress: summer casual ~ <span class="aside">bare feet welcome</span></p>
  <p class="line details-3"><span class="big">C</span>ocktail food provided</p>
  <p class="line details-4"><span class="big">BYO</span> ~ <span class="aside">but only if you insist</span></p>

  <p class="line friends-1">If you have some friends or neighbours that you like to</p>
  <p class="line friends-2">hang out with, we would love to meet.</p>
  <p class="line friends-3">Bring them with you!</p>

  <p class="line rsvp-1"><span class="big">A</span>n <span class="big">RSVP</span> for catering would be nice. <span class="big">T</span>ext <span class="big">M</span>ark</p>
  <p class="line rsvp-2">xxx xxxxxx or <span class="big">L</span>isa yyy yyyyy before <span class="big">X</span>mas please.</p>
</main>
</body>
</html>
```